Helping Seniors and their families start the discussion about driver safety, and explore options to preserve senior independence.
Target Market(s)
Seniors and their families
Industry/Entity Type
Non Profit
Number of Pages Required
4 page
Font styles to use
Sans Serif
Requirements
Must have
- Logo
- Application for Amber Crossings Registration

Nice to have
- Colorful, and designed for Senior Citizens and their Families

```html
<!DOCTYPE html>
<html lang="en">
<head>
<meta charset="utf-8">
<title>Contact – Amber Crossings</title>
<link href="https://fonts.googleapis.com/css2?family=Lato:wght@400;700;900&display=swap" rel="stylesheet">
<style>
:root{
  --green:#0a8a3e;
  --green-btn:#56c372;
  --green-icon:#4cc06a;
  --blue:#2a9fd8;
  --ink:#333;
  --text:#555;
  --muted:#999;
  --band:#f1f1f1;
  --line:#d8d8d8;
  --footer:#2b2b2b;
  --footer-text:#8a8a8a;
  --footer-head:#c9c9c9;
}
*{box-sizing:border-box;margin:0;padding:0}
html,body{width:1040px;height:1200px;overflow:hidden}
body{font-family:'Lato',sans-serif;color:var(--text);background:#fff;position:relative}
.abs{position:absolute}
.brand{display:flex;align-items:center;gap:8px;font-weight:900;font-size:21px;line-height:1;color:var(--green);letter-spacing:-.2px}
.brand .dot{width:16px;height:16px;border-radius:50%;background:currentColor;flex:none}
.brand span{display:block;width:110px}
.site-header{left:0;top:0;width:1040px;height:106px}
.site-header .brand{left:64px;top:32px}
.nav{left:354px;top:46px;display:flex;gap:0;font-size:15px;color:var(--text)}
.nav a{position:absolute;white-space:nowrap;text-decoration:none;color:inherit}
.nav a.active{color:var(--ink)}
.nav a.active::after{content:"";position:absolute;left:0;right:0;top:22px;height:2px;background:var(--blue)}
.reservation{left:838px;top:38px;display:flex;gap:10px;align-items:center}
.reservation small{display:block;font-size:12.5px;color:var(--ink)}
.reservation strong{display:block;font-size:17.5px;font-weight:400;color:#222;margin-top:1px}
.hero{left:0;top:106px;width:1040px;height:120px;background:var(--band);text-align:center}
.hero h1{font-size:26px;font-weight:700;color:#444;margin-top:30px}
.hero p{font-size:17px;color:var(--muted);margin-top:8px}
.field label{display:block;font-size:12.5px;color:var(--ink);margin-bottom:6px}
.field label b{color:var(--green-btn);font-weight:400}
.field .box{border:1px solid var(--line);border-radius:4px;background:#fff}
.send{left:434px;top:521px;width:172px;height:41px;border-radius:21px;background:var(--green-btn);color:#fff;font-weight:900;font-size:12px;letter-spacing:1.6px;display:flex;align-items:center;justify-content:center}
.map{left:0;top:610px;width:1040px;height:403px;background:linear-gradient(135deg,#f3f3f3,#ececec 50%,#f4f4f4)}
.card{left:362px;top:694px;width:319px;height:234px;background:#fff;box-shadow:0 2px 10px rgba(0,0,0,.12)}
.card .brand{position:absolute;left:96px;top:38px}
.card hr{position:absolute;left:8px;right:8px;top:108px;border:0;border-top:1px solid #eee}
.card .addr{position:absolute;left:99px;top:139px;font-size:12.5px;line-height:21px;color:var(--text)}
.card svg{position:absolute;left:65px;top:142px}
.site-footer{left:0;top:1013px;width:1040px;height:187px;background:var(--footer)}
.site-footer .brand{position:absolute;left:64px;top:52px;color:#9a9a9a}
.copy{left:64px;top:125px;font-size:13px;color:#c8c8c8}
.col{top:52px}
.col h3{font-size:17px;font-weight:400;color:var(--footer-head);margin-bottom:17px}
.col li{list-style:none;font-size:12.5px;color:var(--footer-text);line-height:25.6px}
.col li.phone{color:var(--green-icon)}
.social{display:flex;gap:26px;margin-top:2px}
.social i{width:18px;height:18px;border-radius:50%;background:var(--green-icon);display:block}
</style>
</head>
<body>

<header class="site-header abs">
  <div class="brand abs"><i class="dot"></i><span>Amber Crossings</span></div>
  <nav class="nav abs">
    <a style="left:0;top:0">Home</a>
    <a style="left:78px;top:0">Services</a>
    <a class="active" style="left:169px;top:0">Application</a>
    <a style="left:281px;top:0">Contact</a>
  </nav>
  <div class="reservation abs">
    <svg width="26" height="24" viewBox="0 0 26 24" fill="none" stroke="var(--blue)" stroke-width="1.6" stroke-linecap="round">
      <path d="M14 3c1-1 2-1 3 0l2 3c.6 1 .3 2-.6 2.5l-1 .6c.6 2 2 4 3.6 5.3l1-.6c.9-.5 2-.3 2.5.6l1 1.6"/>
      <path d="M2 20l1 2M6 18l1.4 3.4M10 17l1.6 4"/>
    </svg>
    <div><small>Reservation line</small><strong>770-555-0148</strong></div>
  </div>
</header>

<section class="hero abs">
  <h1>Contact</h1>
  <p>Get in touch with Amber Crossings</p>
</section>

<form class="contact-form">
  <div class="field abs" style="left:234px;top:279px"><label>First name <b>*</b></label><div class="box" style="width:183px;height:34px"></div></div>
  <div class="field abs" style="left:429px;top:279px"><label>Last name <b>*</b></label><div class="box" style="width:183px;height:34px"></div></div>
  <div class="field abs" style="left:624px;top:279px"><label>E-mail <b>*</b></label><div class="box" style="width:183px;height:34px"></div></div>
  <div class="field abs" style="left:234px;top:348px"><label>Your message <b>*</b></label><div class="box" style="width:573px;height:130px"></div></div>
  <div class="send abs">SEND MESSAGE</div>
</form>

<section class="map abs" role="img" aria-label="Street map of the neighbourhood around the office">
  <svg class="abs" style="left:786px;top:182px" width="14" height="18" viewBox="0 0 14 18"><path d="M7 0a7 7 0 0 1 7 7c0 5-7 11-7 11S0 12 0 7a7 7 0 0 1 7-7z" fill="var(--green-icon)"/><circle cx="7" cy="7" r="2.6" fill="#fff"/></svg>
</section>

<div class="card abs">
  <div class="brand"><i class="dot"></i><span>Amber Crossings</span></div>
  <hr>
  <svg width="14" height="18" viewBox="0 0 14 18"><path d="M7 0a7 7 0 0 1 7 7c0 5-7 11-7 11S0 12 0 7a7 7 0 0 1 7-7z" fill="var(--green-icon)"/><circle cx="7" cy="7" r="2.6" fill="#fff"/></svg>
  <div class="addr">Amber Crossings<br>Maple Ridge Road Suite 210-118<br>Alder Falls, Georgia 30091</div>
</div>

<footer class="site-footer abs">
  <div class="brand"><i class="dot"></i><span>Amber Crossings</span></div>
  <p class="copy abs">© Amber Crossings 2017</p>
  <div class="col abs" style="left:298px">
    <h3>Contact</h3>
    <ul><li>Amber Crossings</li><li>Maple Ridge Road Suite 210-118</li><li>Alder Falls, Georgia 30091</li><li class="phone">✆ 678-555-0192</li></ul>
  </div>
  <div class="col abs" style="left:531px">
    <h3>Links</h3>
    <ul><li>Lorem ipsum dolor amet</li><li>Doler sit amet met</li><li>Lorem ipsum dolor amet</li><li>Doler sit amet met</li></ul>
  </div>
  <div class="col abs" style="left:766px">
    <h3>Follow us</h3>
    <div class="social"><i></i><i></i><i></i></div>
  </div>
</footer>

</body>
</html>
```